The goal of this postcard is to get homeowners who have magazines and comics laying around their house to call or email me so I can purchase these from them. I then sell these on tradevale. The name of my business is Marty K's Keepsakes, martyks@mailbrook.net 513-846-2937. Here are some of the ideas I wanted to include:

Do you have magazines, Comic books, artwork or other paper products lying around your house collecting dust?
Before you throw them away or recycle them, let Marty K's Keepsakes make you a cash offer.
Call or email us to schedule a free quote
Looking for small collections to whole basement, attic or garage cleanouts.
We do all the heavy lifting so you don't need to raise a finger.
We are friendly, respectful, professional, and family owned and operated in Southwest Ohio.

```html
<!DOCTYPE html>
<html lang="en">
<head>
<meta charset="utf-8">
<title>Marty K's Keepsakes — Postcard</title>
<link href="https://fonts.googleapis.com/css2?family=Roboto+Condensed:wght@400;700&display=swap" rel="stylesheet">
<style>
  :root{
    --page:#eceef1;
    --white:#ffffff;
    --ink:#141414;
    --brand-blue:#1468b8;
    --stripe-blue:#1463b5;
    --panel-top:#1f78c4;
    --panel-bottom:#17509e;
    --pill-blue:#2ab0e6;
  }
  html,body{margin:0;padding:0;overflow:hidden}
  body{
    width:1200px;height:883px;background:var(--page);
    font-family:"Roboto Condensed",Arial,sans-serif;
    position:relative;
  }
  .postcard{
    position:absolute;left:20px;top:51px;width:1160px;height:780px;
    background:var(--white);overflow:hidden;
    box-shadow:0 2px 10px rgba(0,0,0,.12);
  }
  .postcard__shapes{position:absolute;inset:0}
  .collage{
    position:absolute;inset:0;
    clip-path:polygon(0 0,401px 0,467px 780px,0 780px);
    background:
      linear-gradient(160deg,rgba(196,46,40,.55) 0%,rgba(232,196,62,.5) 30%,rgba(70,140,90,.45) 55%,rgba(190,60,50,.5) 78%,rgba(90,130,190,.45) 100%),
      linear-gradient(90deg,#8a7a6a,#b59b6a);
  }
  .brand-name{
    position:absolute;left:520px;right:42px;top:38px;margin:0;
    text-align:right;color:var(--brand-blue);
    font-weight:700;font-size:44px;line-height:52px;letter-spacing:.5px;text-transform:uppercase;
    white-space:nowrap;
  }
  .headline{
    position:absolute;left:473px;top:124px;width:680px;margin:0;
    color:var(--ink);font-weight:700;font-size:29px;line-height:42px;text-transform:uppercase;
    white-space:nowrap;
  }
  .offer{
    position:absolute;left:473px;top:268px;width:660px;margin:0;
    color:var(--brand-blue);font-weight:700;font-size:25px;line-height:36px;
    white-space:nowrap;
  }
  .services{
    position:absolute;left:550px;top:425px;width:530px;margin:0;
    color:var(--white);font-size:19px;line-height:31px;text-align:center;
    white-space:nowrap;
  }
  .cta{
    position:absolute;left:500px;right:30px;top:628px;margin:0;
    color:var(--white);font-weight:700;font-size:23px;text-align:center;text-transform:uppercase;
    white-space:nowrap;
  }
  .contact{
    position:absolute;left:500px;right:30px;top:680px;
    display:flex;justify-content:center;align-items:center;gap:26px;color:var(--white);
    white-space:nowrap;
  }
  .contact__item{display:flex;align-items:center;gap:12px}
  .contact__phone{font-weight:700;font-size:34px}
  .contact__email{font-size:31px}
</style>
</head>
<body>
  <article class="postcard">
    <svg class="postcard__shapes" width="1160" height="780" viewBox="0 0 1160 780" aria-hidden="true">
      <defs>
        <linearGradient id="panelGradient" x1="0" y1="0" x2="0.3" y2="1">
          <stop offset="0" stop-color="var(--panel-top)"/>
          <stop offset="1" stop-color="var(--panel-bottom)"/>
        </linearGradient>
      </defs>
      <polygon points="401,0 432,0 498,780 467,780" fill="var(--stripe-blue)"/>
      <polygon points="473,492 1160,492 1160,780 497,780" fill="url(#panelGradient)"/>
      <path d="M596,380 H1160 V579 H596 A99.5,99.5 0 0 1 596,380 Z" fill="var(--pill-blue)"/>
    </svg>

    <div class="collage" role="img" aria-label="Collage of vintage magazine and comic book covers"></div>

    <h1 class="brand-name">Marty K's Keepsakes</h1>
    <h2 class="headline">Do you have magazines, comic books, artwork<br>or other paper products lying around your<br>house collecting dust?</h2>
    <p class="offer">Before you throw them away or recycle them,<br>let Marty K's Keepsakes make you a cash offer.</p>
    <p class="services">Looking for small collections to whole basement,<br>attic or garage cleanouts. We do all the heavy lifting so you don't need<br>to raise a finger. We are friendly, respectful, professional, and family<br>owned and operated in Southwest Ohio</p>
    <p class="cta">Call or email us to schedule a free quote</p>
    <div class="contact">
      <span class="contact__item">
        <svg width="34" height="34" viewBox="0 0 34 34" aria-hidden="true">
          <circle cx="17" cy="17" r="15" fill="none" stroke="#fff" stroke-width="3"/>
          <path d="M12 9 L15 12 L13 15 Q15 19 19 21 L22 19 L25 22 L22 25 Q13 24 9 12 Z" fill="#fff"/>
        </svg>
        <span class="contact__phone">513-846-2937</span>
      </span>
      <span class="contact__item">
        <svg width="30" height="24" viewBox="0 0 30 24" aria-hidden="true">
          <path d="M2 10 L15 2 L28 10 V22 H2 Z" fill="#fff"/>
          <path d="M5 12 L15 18 L25 12" fill="none" stroke="var(--panel-top)" stroke-width="2"/>
        </svg>
        <span class="contact__email">martyks@mailbrook.net</span>
      </span>
    </div>
  </article>
</body>
</html>
```